Business Card Design

New business card design

Target Market(s)

Residential & Commercial Property Managers

Industry/Entity Type

Plumbing Services

Contact Information for Business Card

Name - Owen Tredgold, title - Director, Phone Number - 0431 862 507, email - owen@rvb-plumbing.com.au, Company ABN - 73 215 904 386,

Font styles to use
Sans Serif

Colors
0054AA
0677BA
7BADD7
CADEEF
E8F1F8

```html
<!DOCTYPE html>
<html lang="en">
<head>
<meta charset="utf-8">
<title>RVB Plumbing Services – Business Card</title>
<link href="https://fonts.googleapis.com/css2?family=Montserrat:wght@400;500;600&display=swap" rel="stylesheet">
<style>
  :root {
    --backdrop: #1b1c1e;
    --card-light: #f4f5f5;
    --card-dark: #1d232a;
    --ink: #1d232a;
    --accent: #2a9fd8;
    --white: #ffffff;
  }
  * { margin: 0; padding: 0; box-sizing: border-box; }
  html, body { width: 1200px; height: 1059px; overflow: hidden; }
  body {
    background: var(--backdrop);
    font-family: "Montserrat", sans-serif;
    position: relative;
  }
  .card {
    position: absolute;
    left: 255px;
    width: 690px;
    height: 392px;
    border-radius: 18px;
    overflow: hidden;
  }
  .card--front { top: 89px; background: var(--card-light); color: var(--ink); }
  .card--back { top: 547px; background: var(--card-dark); }

  .brand {
    position: absolute;
    display: flex;
    align-items: center;
    gap: 10px;
    font-weight: 500;
    letter-spacing: 0.5px;
    white-space: nowrap;
  }
  .brand__dot { width: 14px; height: 14px; border-radius: 50%; background: var(--accent); flex: none; }
  .card--front .brand { right: 43px; top: 80px; font-size: 26px; color: var(--ink); }
  .card--back .brand { left: 0; right: 0; justify-content: center; top: 172px; font-size: 38px; color: var(--white); }

  .person { position: absolute; left: 40px; top: 212px; }
  .person__name { font-size: 27px; font-weight: 600; color: var(--accent); line-height: 1.1; }
  .person__role { font-size: 17px; font-weight: 400; margin-top: 2px; }

  .divider { position: absolute; left: 40px; right: 43px; top: 283px; height: 1px; background: var(--accent); }

  .contact { position: absolute; left: 40px; top: 300px; list-style: none; font-size: 17.5px; }
  .contact li { display: flex; align-items: center; gap: 8px; height: 26px; }
  .contact svg { width: 13px; height: 13px; fill: var(--accent); }

  .abn { position: absolute; right: 43px; top: 325px; font-size: 17.5px; }
  .abn__label { color: var(--accent); }

  .band { position: absolute; left: 0; bottom: 0; width: 100%; height: 18px; }
</style>
</head>
<body>
  <section class="card card--front">
    <div class="brand"><span class="brand__dot"></span>rvb plumbing services</div>

    <div class="person">
      <p class="person__name">Owen Tredgold</p>
      <p class="person__role">Director</p>
    </div>

    <div class="divider"></div>

    <ul class="contact">
      <li>
        <svg viewBox="0 0 24 24" aria-hidden="true"><path d="M6.6 10.8a15.1 15.1 0 0 0 6.6 6.6l2.2-2.2a1 1 0 0 1 1-.25 11.4 11.4 0 0 0 3.6.57 1 1 0 0 1 1 1V20a1 1 0 0 1-1 1A17 17 0 0 1 3 4a1 1 0 0 1 1-1h3.5a1 1 0 0 1 1 1c0 1.25.2 2.45.57 3.57a1 1 0 0 1-.25 1z"/></svg>
        0431 862 507
      </li>
      <li>
        <svg viewBox="0 0 24 24" aria-hidden="true"><path d="M2 5h20v14H2z M2 5l10 8 10-8" fill="none" stroke="#2a9fd8" stroke-width="0"/><path d="M2 5h20l-10 8z"/><path d="M2 7l10 8 10-8v12H2z"/></svg>
        owen@rvb-plumbing.com.au
      </li>
    </ul>

    <p class="abn"><span class="abn__label">ABN</span> - 73 215 904 386</p>

    <svg class="band" viewBox="0 0 690 18" preserveAspectRatio="none" aria-hidden="true">
      <polygon points="0,0 340,0 322,18 0,18" fill="#1d232a"/>
      <polygon points="360,0 690,0 690,18 336,18" fill="#2a9fd8"/>
    </svg>
  </section>

  <section class="card card--back">
    <div class="brand"><span class="brand__dot"></span>rvb plumbing services</div>
  </section>
</body>
</html>
```